Business card for new consulting business - Brackenvale Enterprises Pty Ltd.

Consulting in the areas of Occupational Health, Safety and Community Relations in the resources (mining) industries. The consultant (me) will work both within Australia and overseas jurisdictions such as South East Asia, Africa , South America etc, often working with third world indigenous communities. The design should suggest a high level of social and environmental responsibility.

```html
<!DOCTYPE html>
<html lang="en">
<head>
<meta charset="utf-8">
<title>Brackenvale Enterprises – Business Card</title>
<link href="https://fonts.googleapis.com/css2?family=Montserrat:wght@700;800&family=Roboto:wght@400&display=swap" rel="stylesheet">
<style>
  :root {
    --bg: #1d1d1d;
    --card: #121212;
    --card-edge: #1a1a1a;
    --green: #3aa13c;
    --green-light: #7cc043;
    --blue: #1d7fd0;
    --blue-deep: #0f5aa8;
    --white: #f2f2f2;
    --rule: #d8d8d8;
  }
  * { margin: 0; padding: 0; box-sizing: border-box; }
  html, body { width: 1200px; height: 1200px; overflow: hidden; }
  body { background: var(--bg); position: relative; font-family: "Roboto", sans-serif; color: var(--white); }

  .card {
    position: absolute;
    left: 170px;
    width: 860px;
    height: 480px;
    background: linear-gradient(135deg, var(--card) 0%, var(--card-edge) 100%);
    box-shadow: 0 14px 30px rgba(0,0,0,.55);
    overflow: hidden;
  }
  .card--back { top: 90px; }
  .card--front { top: 630px; }

  .brand {
    display: flex; align-items: center; gap: 14px;
    font-family: "Montserrat", sans-serif; font-weight: 800;
    color: var(--green); text-transform: uppercase; line-height: 1.1;
  }
  .brand__dot { width: 22px; height: 22px; border-radius: 50%; background: var(--green); flex: none; }

  .card--back .brand { position: absolute; left: 0; right: 0; top: 190px; justify-content: center; font-size: 30px; }
  .card--back .site { position: absolute; left: 0; right: 0; top: 330px; text-align: center; font-size: 17px; letter-spacing: 1px; }

  .person { position: absolute; left: 70px; top: 55px; font-family: "Montserrat", sans-serif; font-weight: 800; text-transform: uppercase; }
  .person__name { color: var(--green); font-size: 30px; }
  .person__role { color: var(--blue); font-size: 17px; margin-top: 2px; }

  .card--front .brand { position: absolute; right: 60px; top: 115px; font-size: 24px; width: 400px; }

  .rule { position: absolute; left: 60px; right: 60px; top: 222px; height: 1px; background: var(--rule); }

  .contacts { position: absolute; left: 60px; top: 240px; list-style: none; font-size: 19px; }
  .contacts li { display: flex; align-items: center; gap: 14px; height: 32px; }
  .contacts svg { width: 20px; height: 20px; fill: var(--blue); }

  .address { position: absolute; right: 60px; top: 244px; text-align: right; font-size: 19px; line-height: 1.45; }

  .band { position: absolute; left: 0; bottom: 0; width: 860px; height: 150px; }
  .band__site { position: absolute; right: 60px; bottom: 20px; font-size: 20px; letter-spacing: .5px; line-height: 24px; }
</style>
</head>
<body>

<section class="card card--back">
  <div class="brand"><span class="brand__dot"></span>Brackenvale Enterprises Pty Ltd</div>
  <p class="site">www.brackenvale.com</p>
</section>

<section class="card card--front">
  <div class="person">
    <p class="person__name">Daniel Harlow</p>
    <p class="person__role">CEO/Founder</p>
  </div>

  <div class="brand"><span class="brand__dot"></span>Brackenvale Enterprises Pty Ltd</div>

  <div class="rule"></div>

  <ul class="contacts">
    <li><svg viewBox="0 0 24 24" aria-hidden="true"><path d="M6.6 10.8a15.1 15.1 0 0 0 6.6 6.6l2.2-2.2a1 1 0 0 1 1-.25 11.4 11.4 0 0 0 3.6.57 1 1 0 0 1 1 1V20a1 1 0 0 1-1 1A17 17 0 0 1 3 4a1 1 0 0 1 1-1h3.5a1 1 0 0 1 1 1c0 1.25.2 2.45.57 3.57a1 1 0 0 1-.25 1z"/></svg>230.555.0142</li>
    <li><svg viewBox="0 0 24 24" aria-hidden="true"><path d="M6 3h12v5H6zM4 9h16a2 2 0 0 1 2 2v6h-4v4H6v-4H2v-6a2 2 0 0 1 2-2zm4 7v3h8v-3z"/></svg>230.555.0178</li>
    <li><svg viewBox="0 0 24 24" aria-hidden="true"><path d="M2 5h20v14H2zm2 2v.4l8 5.2 8-5.2V7zm0 2.8V17h16V9.8l-8 5.2z"/></svg>daniel@brackenvale.com</li>
  </ul>

  <p class="address">48 Ridgeway Lane<br>Suite B, Marlow, CA 90417</p>

  <svg class="band" viewBox="0 0 860 150" preserveAspectRatio="none" aria-hidden="true">
    <defs>
      <linearGradient id="greenFill" x1="0" x2="1" y1="0" y2="0">
        <stop offset="0" stop-color="#2f8f3e"/>
        <stop offset="1" stop-color="#7cc043"/>
      </linearGradient>
      <linearGradient id="blueFill" x1="0" x2="1">
        <stop offset="0" stop-color="#1d7fd0"/>
        <stop offset="1" stop-color="#0f5aa8"/>
      </linearGradient>
    </defs>
    <path d="M0 22 Q 430 88 860 54 L860 150 L0 150 Z" fill="url(#blueFill)"/>
    <path d="M0 30 Q 430 96 860 66 L860 150 L0 150 Z" fill="#ffffff"/>
    <path d="M0 36 Q 430 102 860 72 L860 150 L0 150 Z" fill="url(#greenFill)"/>
  </svg>
  <p class="band__site">www.brackenvale.com</p>
</section>

</body>
</html>
```